Criação de Cartao de Visita para Computador & Internet
" Nossos clientes fazem o outsorcing da TI para nós, assim cuidamos de todos os recursos se serviços de TI, também vendemos hardwares e softwares "

```html
<!DOCTYPE html>
<html lang="pt-BR">
<head>
<meta charset="UTF-8">
<title>Nuvte Corp – Cartões de Visita</title>
<link href="https://fonts.googleapis.com/css2?family=Open+Sans:wght@400;600;700&display=swap" rel="stylesheet">
<style>
  :root{
    --bg:#e4e6e8;
    --card:#ffffff;
    --blue:#1b78c2;
    --blue-light:#3aa6e2;
    --grey-band:#c9cdd1;
    --green:#6aae36;
    --red:#d02b2b;
    --text:#4a4f55;
    --muted:#8a9096;
  }
  *{margin:0;padding:0;box-sizing:border-box}
  html,body{width:1200px;height:1200px;overflow:hidden}
  body{
    background:var(--bg);
    font-family:"Open Sans",Arial,sans-serif;
    display:flex;flex-direction:column;align-items:center;justify-content:center;gap:36px;
  }
  .card{
    position:relative;width:600px;height:343px;background:var(--card);
    overflow:hidden;box-shadow:0 6px 18px rgba(0,0,0,.12);
  }
  .card .bands{position:absolute;inset:0;width:100%;height:100%}

  /* front */
  .brand{position:absolute;left:70px;top:128px;display:flex;align-items:center;gap:16px}
  .brand__dot{width:72px;height:72px;border-radius:50%;background:var(--blue)}
  .brand__name{font-size:38px;font-weight:700;color:var(--blue);letter-spacing:.5px}

  /* contact */
  .contact{position:absolute;left:48px;top:44px;width:420px}
  .contact__head{display:flex;align-items:center;gap:10px}
  .contact__mark{width:26px;height:26px;background:var(--blue)}
  .contact__name{font-size:26px;font-weight:600;color:var(--blue);line-height:1}
  .contact__role{font-size:11px;color:var(--muted);margin:4px 0 0 36px}
  .contact__division{font-size:17px;font-weight:700;color:var(--red);margin:18px 0 14px}
  .contact__list{list-style:none;font-size:13px;color:var(--text)}
  .contact__list li{display:flex;align-items:center;gap:9px;margin-bottom:7px}
  .contact__list svg{width:18px;height:18px;flex:none}

  /* services */
  .services__watermark{position:absolute;left:230px;top:100px;width:160px;height:160px;border-radius:50%;background:var(--blue);opacity:.06}
  .services__col{position:absolute;top:46px;width:250px}
  .services__col--it{left:38px}
  .services__col--events{left:328px}
  .services__divider{position:absolute;left:305px;top:46px;width:1px;height:250px;background:var(--grey-band)}
  .services__title{font-size:17px;font-weight:700;letter-spacing:.3px}
  .services__subtitle{font-size:10px;color:var(--muted);margin:2px 0 16px}
  .services__col--it .services__title{color:var(--green)}
  .services__col--events .services__title{color:var(--red)}
  .services__list{list-style:none;font-size:12.5px;color:var(--text)}
  .services__list li{display:flex;align-items:flex-start;gap:8px;margin-bottom:9px;line-height:1.25}
  .services__list li::before{content:"";width:7px;height:7px;border-radius:50%;margin-top:5px;flex:none}
  .services__col--it li::before{background:var(--green)}
  .services__col--events li::before{background:var(--red)}
</style>
</head>
<body>

  <!-- Frente -->
  <section class="card card--front">
    <svg class="bands" viewBox="0 0 600 343" preserveAspectRatio="none" aria-hidden="true">
      <polygon points="360,343 600,230 600,250 405,343" fill="var(--grey-band)"/>
      <polygon points="405,343 600,250 600,343" fill="var(--blue)"/>
      <polygon points="470,343 600,282 600,343" fill="var(--blue-light)"/>
    </svg>
    <div class="brand">
      <span class="brand__dot"></span>
      <span class="brand__name">Nuvte Corp</span>
    </div>
  </section>

  <!-- Contato -->
  <section class="card card--contact">
    <svg class="bands" viewBox="0 0 600 343" preserveAspectRatio="none" aria-hidden="true">
      <polygon points="0,300 250,343 0,343" fill="var(--grey-band)"/>
      <polygon points="0,312 600,300 600,343 0,343" fill="var(--blue)"/>
      <polygon points="0,330 600,320 600,343 0,343" fill="var(--blue-light)"/>
    </svg>
    <div class="contact">
      <div class="contact__head">
        <span class="contact__mark"></span>
        <span class="contact__name">Marina Couto</span>
      </div>
      <p class="contact__role">Gerente Comercial</p>
      <p class="contact__division">DIVISÃO DE EVENTOS</p>
      <ul class="contact__list">
        <li><svg viewBox="0 0 18 18"><rect width="18" height="18" rx="2" fill="var(--blue)"/><path d="M5 4l2 0 1 3-1.5 1a7 7 0 0 0 3.5 3.5l1-1.5 3 1 0 2a1 1 0 0 1-1 1A10 10 0 0 1 4 5a1 1 0 0 1 1-1z" fill="#fff"/></svg>11 3200-4100 (SP)</li>
        <li><svg viewBox="0 0 18 18"><rect width="18" height="18" rx="2" fill="var(--blue)"/><path d="M5 4l2 0 1 3-1.5 1a7 7 0 0 0 3.5 3.5l1-1.5 3 1 0 2a1 1 0 0 1-1 1A10 10 0 0 1 4 5a1 1 0 0 1 1-1z" fill="#fff"/></svg>0800 600 1234 (Demais Localidades)</li>
        <li><svg viewBox="0 0 18 18"><rect width="18" height="18" rx="2" fill="var(--blue)"/><rect x="6" y="3" width="6" height="12" rx="1" fill="#fff"/><rect x="7" y="5" width="4" height="7" fill="var(--blue)"/></svg>11 90000-1234</li>
        <li><svg viewBox="0 0 18 18"><rect width="18" height="18" rx="2" fill="var(--blue)"/><rect x="3.5" y="5" width="11" height="8" fill="#fff"/><path d="M3.5 5l5.5 4.5 5.5-4.5" stroke="var(--blue)" fill="none"/></svg>marina.couto@nuvtecorp.com.br</li>
      </ul>
    </div>
  </section>

  <!-- Serviços -->
  <section class="card card--services">
    <span class="services__watermark"></span>
    <div class="services__col services__col--it">
      <h2 class="services__title">DIVISÃO DE TI</h2>
      <p class="services__subtitle">Soluções em Tecnologia da Informação</p>
      <ul class="services__list">
        <li>Administração e Suporte de TI / Outsourcing</li>
        <li>Cloud Services</li>
        <li>Cabeamento e Infraestrutura de Redes</li>
        <li>Consultoria e Projetos de TI</li>
        <li>Segurança e Proteção de Dados</li>
      </ul>
    </div>
    <span class="services__divider"></span>
    <div class="services__col services__col--events">
      <h2 class="services__title">DIVISÃO DE EVENTOS</h2>
      <p class="services__subtitle">Soluções em gestão de eventos</p>
      <ul class="services__list">
        <li>Seminários</li>
        <li>Congressos</li>
        <li>Convenções</li>
        <li>Feiras</li>
        <li>Workshops</li>
        <li>Networking</li>
        <li>Coquetéis Empresariais</li>
      </ul>
    </div>
  </section>

</body>
</html>
```